Packaging design for a Deli Shop "TORVO Gourmet"

We need a packaging design for a new Deli Business we are opening soon. We produce food to be packaged and sold either fresh or frozen in transparent disposable plastic boxes, cardboard boxes and finally delivered in a bag (Paper, plastic or shopping bag whatever goes best with the design) to take out. The food we generally pack are salads, lasagnas, ceviches, sandwiches, cookies, granola, dips, etc.

The name of the company is "TORVO Gourmet" Check our website for reference: www.torvogourmet-example.com

We have a logo and a name we want to maintain (attached).

The product will be sold in our new deli store, that is inspired in big cities delikatessen, quite modern and trendy. It also delivers a message that everything we sell is high quality, artisan (not massive or mainstream) and great in flavors.

Packaging must communicate freshness, great flavor, high quality and high price.

Packaging must be feasible to produce and print easily without any complex or impossible to implement packaging, (preferrable to be done or easy to adapt from generic packaging).

All our communication will be in Spanish so please do not depend on english for the design. If english or any other language is used, please be sure its understandable in almost any country (ie Basic English, Italian).

Same packaging (labeling or boxes and bags) will be used, just changing the name of the product inside according to the product.

Most of our product will be displayed in refrigerators and freezers.
Updates

I just uploaded a visual brief of the packaging examples we would like to have.

Looking forward to see your designs.
Thank you

Project Deadline Extended
Reason: Some designers who said will participate havent submitted their deaigns, and still what is being submitted is not fully complying with the requirements. Thank you

Target Market(s)

The main target is High SEL, between 24 and 40, mostly woman

Industry/Entity Type

Communication

Requirements
Must have

Nice to have
• Please take a look at my website www.torvogourmet-example.com to see the kind of coloring we are aiming to have.

Give the impression of being "Green"...

Include "Kraft" color paper / Brown paper color
Should not have
• Complex packaging difficult to implement in a simple print shop.
Expensive items.

```html
<!DOCTYPE html>
<html lang="es">
<head>
<meta charset="utf-8">
<title>TORVO Gourmet — etiquetas y cintillos</title>
<link rel="stylesheet" href="https://fonts.googleapis.com/css2?family=Work+Sans:wght@300&family=Josefin+Sans:wght@400&family=Dancing+Script:wght@600&display=swap">
<style>
  :root {
    --kraft: #e4c5aa;
    --salad-green: #2aa05a;
    --salad-lime: #7fff00;
    --salad-yellow: #e6ff00;
    --salad-teal: #1e8f7a;
    --dips-blue: #0a12ff;
    --sandwich-brown: #5b4a24;
    --sandwich-red: #ff2a1a;
    --dessert-purple: #8000ff;
    --dessert-check: #b8ef6a;
    --caption: #6a6a6a;
    --paper: #ffffff;
  }
  html, body {
    margin: 0;
    padding: 0;
    width: 1192px;
    height: 1200px;
    overflow: hidden;
    background: var(--paper);
  }
  .sheet { display: block; width: 1192px; height: 1200px; }
  .caption {
    font-family: "Work Sans", sans-serif;
    font-weight: 300;
    font-size: 29px;
    fill: var(--caption);
  }
  .brand {
    font-family: "Josefin Sans", sans-serif;
    font-weight: 400;
  }
  .category {
    font-family: "Dancing Script", cursive;
    font-weight: 600;
  }
  .product {
    font-family: "Josefin Sans", sans-serif;
    font-weight: 400;
  }
  .kraft { fill: var(--kraft); }
</style>
</head>
<body>
<svg class="sheet" viewBox="0 0 1410 1420" xmlns="http://www.w3.org/2000/svg">
  <defs>
    <linearGradient id="salad-pattern-tone" x1="0" y1="0" x2="1" y2="1">
      <stop offset="0" stop-color="#9fd84a"/>
      <stop offset="0.5" stop-color="#6fc25a"/>
      <stop offset="1" stop-color="#b6e83a"/>
    </linearGradient>
    <linearGradient id="sandwich-wrap-tone" x1="0" y1="0" x2="0" y2="1">
      <stop offset="0" stop-color="#a8f240"/>
      <stop offset="1" stop-color="#b9e07a"/>
    </linearGradient>
    <linearGradient id="gingham-tone" x1="0" y1="0" x2="1" y2="0">
      <stop offset="0" stop-color="#c6f08a"/>
      <stop offset="1" stop-color="var(--dessert-check)"/>
    </linearGradient>

    <clipPath id="salad-clip">
      <rect x="150" y="200" width="299" height="330"/>
    </clipPath>
    <clipPath id="dips-clip">
      <path d="M617 380 A187 187 0 0 1 991 380 L991 568 L804 568 A187 187 0 0 1 617 380 Z"/>
    </clipPath>
    <clipPath id="sandwich-clip">
      <rect x="302" y="800" width="182" height="122"/>
    </clipPath>
    <clipPath id="dessert-clip">
      <rect x="1060" y="990" width="295" height="286"/>
    </clipPath>
  </defs>

  <!-- cintillo ensalada -->
  <g class="salad-sleeve">
    <text class="caption" x="243" y="95">cintillo ensalada</text>
    <rect x="265" y="125" width="184" height="552" fill="url(#salad-pattern-tone)"
          role="img" aria-label="Patrón decorativo de hojas verdes y amarillas sobre kraft"/>
    <g clip-path="url(#salad-clip)">
      <circle class="kraft" cx="308" cy="365" r="142"/>
      <rect x="150" y="394" width="299" height="140" fill="var(--salad-lime)"
            clip-path="circle(142px at 158px -29px)"/>
    </g>
    <g clip-path="url(#salad-clip)">
      <path d="M166 394 L449 394 L449 520 L166 520 Z" fill="var(--salad-lime)"
            style="clip-path: circle(142px at 142px -29px);"/>
    </g>
    <text class="brand" x="314" y="350" text-anchor="middle" fill="var(--salad-green)">
      <tspan font-size="58">TORVO</tspan>
      <tspan x="314" dy="30" font-size="22" letter-spacing="6">Gourmet</tspan>
    </text>
    <text class="category" x="316" y="440" text-anchor="middle" font-size="36" fill="var(--salad-teal)">ensaladas</text>
    <text class="product" x="318" y="469" text-anchor="middle" font-size="18" fill="var(--salad-teal)">Risoni Mediterranea</text>
  </g>

  <!-- sticker -->
  <g class="dips-sticker">
    <text class="caption" x="800" y="158" text-anchor="middle">sticker</text>
    <g clip-path="url(#dips-clip)">
      <rect class="kraft" x="617" y="193" width="374" height="376"/>
      <rect x="617" y="414" width="374" height="155" fill="var(--dips-blue)"/>
    </g>
    <text class="brand" x="808" y="368" text-anchor="middle" fill="var(--dips-blue)">
      <tspan font-size="92">TORVO</tspan>
      <tspan x="808" dy="38" font-size="26" letter-spacing="8">Gourmet</tspan>
    </text>
    <text class="category" x="812" y="470" text-anchor="middle" font-size="50" fill="var(--kraft)">dips</text>
    <text class="product" x="812" y="516" text-anchor="middle" font-size="22" fill="var(--kraft)">4 quesos</text>
  </g>

  <!-- empaque sandwich -->
  <g class="sandwich-pack">
    <text class="caption" x="189" y="788">empaque sandwich</text>
    <polygon points="36,815 36,1368 257,1368" fill="url(#sandwich-wrap-tone)"
             role="img" aria-label="Patrón decorativo de óvalos verde lima sobre kraft"/>
    <path fill-rule="evenodd" fill="var(--sandwich-red)"
          d="M302 814 H484 V1368 H302 Z M343 1018 V1295 H440 V1018 Z"
          role="img" aria-label="Fondo rojo con lunares blancos y ventana transparente"/>
    <g clip-path="url(#sandwich-clip)">
      <circle class="kraft" cx="393" cy="905" r="92"/>
    </g>
    <rect x="302" y="922" width="182" height="75" fill="var(--sandwich-brown)"/>
    <text class="brand" x="396" y="895" text-anchor="middle" fill="var(--sandwich-brown)">
      <tspan font-size="36">TORVO</tspan>
      <tspan x="396" dy="19" font-size="14" letter-spacing="4">Gourmet</tspan>
    </text>
    <text class="category" x="398" y="950" text-anchor="middle" font-size="24" fill="var(--kraft)">sandwiches</text>
    <text class="product" x="401" y="970" text-anchor="middle" font-size="12" fill="var(--kraft)">
      <tspan>pavo a las finas</tspan>
      <tspan x="401" dy="13">hierbas</tspan>
    </text>
  </g>

  <!-- cintillo postres -->
  <g class="dessert-sleeve">
    <text class="caption" x="572" y="1109">cintillo postres</text>
    <rect x="562" y="1172" width="793" height="104" fill="url(#gingham-tone)"
          role="img" aria-label="Patrón vichy verde claro"/>
    <g clip-path="url(#dessert-clip)">
      <circle class="kraft" cx="1216" cy="1138" r="140"/>
      <rect x="1060" y="1162" width="295" height="114" fill="var(--dessert-purple)"
            style="clip-path: circle(140px at 156px -24px);"/>
    </g>
    <text class="brand" x="1221" y="1125" text-anchor="middle" fill="var(--dessert-purple)">
      <tspan font-size="62">TORVO</tspan>
      <tspan x="1221" dy="30" font-size="21" letter-spacing="7">Gourmet</tspan>
    </text>
    <text class="category" x="1222" y="1204" text-anchor="middle" font-size="36" fill="var(--kraft)">postres</text>
    <text class="product" x="1229" y="1234" text-anchor="middle" font-size="18" fill="var(--kraft)">brownies</text>
  </g>
</svg>
</body>
</html>
```